Präsentationsvorlagen für IT-Systemhaus
Zielgruppe
Wir sind ein IT-Systemhaus, das Beratung und Dienstleistungen für kleine und mittelständische Unternehmen im gesamten deutschsprachigen Raum anbietet. Wir möchten uns gerne eine neue Präsentationsvorlage für PowerPoint erstellen lassen, welche sowohl für Unternehmenspräsentationen, als auch für Kundenpräsentationen im Projektumfeld gut verwendet werden kann.
Aufgabenstellung
Das Design sollte im 16:9 Format angelegt werden. Als Schriftart verwenden Sie bitte OpenSans und ggf. für die Überschriften Armata. Ansonsten sind Sie in der Gestaltung frei.
Vielen Dank für Ihre Mühe!

```html
<!DOCTYPE html>
<html lang="de">
<head>
<meta charset="utf-8">
<title>Präsentationsvorlage – Inhaltsfolie</title>
<link href="https://fonts.googleapis.com/css2?family=Armata&family=Open+Sans:wght@300;400&display=swap" rel="stylesheet">
<style>
  :root {
    --brand-red: #a62e2e;
    --text-grey: #666666;
    --white: #ffffff;
  }
  html, body {
    margin: 0;
    padding: 0;
    overflow: hidden;
    background: var(--white);
  }
  .slide {
    position: relative;
    width: 1200px;
    height: 669px;
    overflow: hidden;
    background: var(--white);
    font-family: "Open Sans", sans-serif;
  }
  .side-panel {
    position: absolute;
    left: 19px;
    top: 0;
    width: 384px;
    height: 645px;
    background: var(--brand-red);
  }
  .side-panel__title {
    position: absolute;
    left: 50px;
    top: 108px;
    margin: 0;
    font-family: "Armata", sans-serif;
    font-weight: 400;
    font-size: 46px;
    letter-spacing: 2px;
    color: var(--white);
  }
  .side-panel__body {
    position: absolute;
    left: 43px;
    top: 193px;
    width: 242px;
    color: var(--white);
    font-weight: 300;
    font-size: 11.2px;
    line-height: 13.6px;
  }
  .side-panel__body p { margin: 0 0 13px; }
  .brand {
    position: absolute;
    right: 46px;
    top: 36px;
    display: flex;
    align-items: center;
    gap: 8px;
    font-family: "Open Sans", sans-serif;
    font-weight: 300;
    font-size: 34px;
    color: var(--text-grey);
    letter-spacing: -0.5px;
  }
  .brand__mark {
    width: 30px;
    height: 30px;
    background: var(--brand-red);
  }
  .content-card {
    position: absolute;
    left: 366px;
    top: 157px;
    width: 759px;
    height: 444px;
    background: var(--white);
    box-shadow: 6px 8px 22px rgba(0,0,0,0.22);
  }
  .content-card__title {
    position: absolute;
    left: 103px;
    top: 43px;
    margin: 0;
    font-family: "Armata", sans-serif;
    font-weight: 400;
    font-size: 46px;
    letter-spacing: 2px;
    color: var(--text-grey);
  }
  .content-card__body {
    position: absolute;
    left: 51px;
    top: 121px;
    width: 650px;
    color: var(--text-grey);
    font-size: 13px;
    line-height: 15.8px;
  }
  .content-card__body p { margin: 0 0 15px; }
  .content-card__body .tight { margin-bottom: 0; }
</style>
</head>
<body>
<div class="slide">
  <aside class="side-panel">
    <h1 class="side-panel__title">Überschrift</h1>
    <div class="side-panel__body">
      <p>Lorem ipsum dolor sit amet, consectetuer adipiscing elit, sed diam nonummy nibh euismod tincidunt ut laoreet dolore magna aliquam erat volutpat. Ut wisi enim ad minim veniam, quis nostrud exerci tation ullamcorper suscipit lobortis nisl ut aliquip ex ea commodo consequat.</p>
      <p>Duis autem vel eum iriure dolor in hendrerit in vulputate velit esse molestie consequat, vel illum dolore eu feugiat nulla facilisis at vero eros et accumsan et iusto odio dignissim qui blandit praesent luptatum zzril delenit augue duis dolore te feugait nulla facilisi.</p>
      <p>Lorem ipsum dolor sit amet, cons ectetuer adipiscing elit, sed diam nonummy nibh euismod tincidunt ut laoreet dolore magna aliquam erat volutpat. Ut wisi enim ad minim veniam, quis nostrud exerci tation ullamcorper suscipit lobortis nisl ut aliquip ex ea commodo consequat.</p>
      <p>Lorem ipsum dolor sit amet, consectetuer adipiscing elit, sed diam nonummy nibh euismod tincidunt ut laoreet dolore</p>
    </div>
  </aside>

  <div class="brand">
    <span class="brand__mark"></span>
    <span class="brand__name">NX-QB GmbH</span>
  </div>

  <section class="content-card">
    <h2 class="content-card__title">Überschrift</h2>
    <div class="content-card__body">
      <p>Lorem ipsum dolor sit amet, consectetuer adipiscing elit, sed diam nonummy nibh euismod tincidunt ut laoreet dolore magna aliquam erat volutpat. Ut wisi enim ad minim veniam, quis nostrud exerci tation ullamcorper suscipit lobortis nisl ut aliquip ex ea commodo consequat. Duis autem vel eum iriure dolor in hendrerit in vulputate velit esse molestie consequat, vel illum dolore eu feugiat nulla facilisis at vero eros et accumsan et iusto odio dignissim qui blandit praesent luptatum zzril delenit augue duis dolore te feugait nulla facilisi.</p>
      <p class="tight">Lorem ipsum dolor sit amet, cons ectetuer adipiscing elit, sed diam nonummy nibh euismod tincidunt ut laoreet dolore magna aliquam erat volutpat. Ut wisi enim ad minim veniam, quis nostrud exerci tation ullamcorper suscipit lobortis nisl ut aliquip ex ea commodo consequat</p>
      <p class="tight">.</p>
      <p>Lorem ipsum dolor sit amet, consectetuer adipiscing elit, sed diam nonummy nibh euismod tincidunt ut laoreet dolore magna aliquam erat volutpat. Ut wisi enim ad minim veniam, quis nostrud exerci tation ullamcorper suscipit lobortis nisl ut aliquip ex ea commodo consequat. Duis autem vel eum iriure dolor in hendrerit in vulputate velit esse molestie consequat, vel illum dolore eu feugiat nulla facilisis at vero eros et accumsan et iusto odio dignissim qui blandit praesent luptatum zzril delenit augue duis dolore te feugait nulla facilisi.</p>
    </div>
  </section>
</div>
</body>
</html>
```